Design a Online payment portal

We have a mobile money transfer company, We now want to provide an online platform for companies to fill in transfer details to, say, 1,000 employees then the transfer list is electronically available to us through the website.

I need a website that basically works like a bank account and people (client) can log on to the website and create accounts.

We the administrators then activate the account once details are provided by them.

Then client then deposits an amount (outside the payment platform) and the administrator can then "load" this as virtual money or as a balance on the client's account.

The platform provides tools for workflows, approvals and rejections, comments, attachments,

After final approval by the client's top boss or whoever is designated as the signatory/approver, we at the back end process the transfer of funds.

but transaction initiators working mostly on excel files may not need so much of the mobile.

The platform should generate notifications every time a transaction happens. it should generate reports as well.

we would also need to charge for each transaction on the platform.

Industry/Entity Type

It Company

```html
<!DOCTYPE html>
<html lang="en">
<head>
<meta charset="utf-8">
<title>Pay Online Safely</title>
<link rel="stylesheet" href="https://fonts.googleapis.com/css2?family=Montserrat:wght@400;500;600&family=Noto+Serif&family=Cinzel:wght@400&display=swap">
<style>
  :root {
    --page-bg: #efefef;
    --ink-dark: #3d3b3c;
    --nav-bg: #f47c66;
    --nav-ink: #2e2a29;
    --green: #3bb878;
    --blue: #3d86c1;
    --field-border: #4fd4f5;
    --field-bg: #efefef;
    --field-ink: #9a9a9a;
    --link: #2a56d6;
    --heading: #1aa0cc;
    --body-ink: #555555;
    --footer-bg: #778489;
    --white: #ffffff;
  }
  * { box-sizing: border-box; margin: 0; padding: 0; }
  html, body { width: 1136px; height: 1200px; overflow: hidden; }
  body {
    position: relative;
    background: var(--page-bg);
    font-family: "Montserrat", Arial, sans-serif;
  }
  .site-header { position: absolute; left: 0; top: 0; width: 1136px; height: 136px; }
  .brand {
    position: absolute; left: 197px; top: 52px;
    font-size: 55px; font-weight: 500; color: var(--ink-dark);
    letter-spacing: 2px; line-height: 1;
  }
  .account-actions { position: absolute; left: 775px; top: 70px; display: flex; gap: 6px; }
  .pill {
    height: 30px; border-radius: 15px; color: var(--white);
    font-size: 15px; font-weight: 600; display: flex; align-items: center; justify-content: center;
  }
  .pill-login { width: 89px; background: var(--green); }
  .pill-signup { width: 89px; background: var(--blue); }

  .main-nav {
    position: absolute; left: 0; top: 136px; width: 1136px; height: 48px;
    background: var(--nav-bg); border-bottom: 1px solid #f8c5b9;
  }
  .main-nav a {
    position: absolute; top: 10px;
    font-family: "Noto Serif", Georgia, serif; font-size: 19px;
    color: var(--nav-ink); text-decoration: none;
  }

  .hero {
    position: absolute; left: 0; top: 184px; width: 1136px; height: 426px;
    background: linear-gradient(100deg, #9fb58c 0%, #d9d9d4 30%, #ecebe7 55%, #dedcd6 75%, #c9c9a0 92%, #a8bb5c 100%);
  }
  .login-form { position: absolute; left: 718px; top: 82px; width: 300px; }
  .field {
    width: 273px; height: 58px; border: 3px solid var(--field-border);
    background: var(--field-bg); color: var(--field-ink);
    font-size: 18px; font-weight: 500; padding-left: 16px;
    display: flex; align-items: center; margin-bottom: 18px;
  }
  .form-row { display: flex; align-items: center; margin-top: 3px; }
  .btn-login {
    width: 115px; height: 39px; border-radius: 20px; background: var(--green);
    color: var(--white); font-size: 19px; font-weight: 500;
    display: flex; align-items: center; justify-content: center;
  }
  .forgot { margin-left: 18px; font-size: 13px; color: var(--link); }

  .intro { position: absolute; left: 100px; top: 662px; width: 870px; text-align: center; }
  .intro h1 {
    font-family: "Cinzel", Georgia, serif; font-weight: 400;
    font-size: 33px; color: var(--heading); margin-bottom: 24px; letter-spacing: 0.5px;
  }
  .intro p { font-size: 15.2px; line-height: 24.6px; color: var(--body-ink); margin-bottom: 24px; }

  .site-footer {
    position: absolute; left: 0; top: 1039px; width: 1136px; height: 161px;
    background: var(--footer-bg);
  }
  .copyright { position: absolute; left: 104px; top: 35px; font-size: 12px; color: var(--white); }
  .social { position: absolute; left: 891px; top: 32px; display: flex; gap: 5px; }
  .social span { width: 28px; height: 28px; background: #5f6b70; display: block; }
</style>
</head>
<body>
  <header class="site-header">
    <div class="brand">LOGO</div>
    <div class="account-actions">
      <div class="pill pill-login">Login</div>
      <div class="pill pill-signup">Signup</div>
    </div>
  </header>

  <nav class="main-nav">
    <a style="left:213px">Home</a>
    <a style="left:312px">About</a>
    <a style="left:410px">Business</a>
    <a style="left:529px">Shop</a>
    <a style="left:618px">Cart</a>
    <a style="left:700px">Checkout</a>
    <a style="left:828px">Contact Us</a>
  </nav>

  <section class="hero" role="img" aria-label="Photo of hands typing on a white laptop while holding a payment card, with a plant and a yellow cup nearby">
    <div class="login-form">
      <div class="field">username</div>
      <div class="field">password</div>
      <div class="form-row">
        <div class="btn-login">Login</div>
        <span class="forgot">forgot password?</span>
      </div>
    </div>
  </section>

  <main class="intro">
    <h1>Pay online SAFELY</h1>
    <p>Lorem ipsum dolor sit amet, consectetuer adipiscing elit, sed diam nonummy nibh euismod tincidunt ut laoreet dolore magna aliquam erat volutpat. Ut wisi enim ad minim veniam, quis nostrud exerci tation ullamcorper suscipit lobortis nisl ut aliquip ex ea commodo consequat. Duis autem vel eum iriure dolor in hendrerit in vulputate velit esse molestie consequat, vel illum dolore eu feugiat nulla facilisis at vero eros et accumsan et iusto odio dignissim qui blandit praesent luptatum zzril delenit augue duis dolore te feugait nulla facilisi.</p>
    <p>Nam liber tempor cum soluta nobis eleifend option congue nihil imperdiet doming id quod mazim placerat facer possim assum. Typi non habent claritatem insitam; est usus legentis in iis qui facit eorum claritatem. Investigationes demonstraverunt lectores legere me lius quod ii legunt saepius. Claritas est etiam processus dynamicus, qui sequitur mutationem consuetudium lectorum. Mirum est notare quam littera gothica</p>
  </main>

  <footer class="site-footer">
    <div class="copyright">© 2015 website</div>
    <div class="social">
      <span role="img" aria-label="Social network link"></span>
      <span role="img" aria-label="Social network link"></span>
    </div>
  </footer>
</body>
</html>
```